Employee Benefits and Insurance Consulting

We are an existing company with over 30 years experience but are changing our name. We would like a simple design with grey tones.

Industry/Entity Type

Insurance

Contact Information for Business Card

Marlow Benefits Consulting
Gerald P Odell CEO
5172 Brackenfield Road
Fenwick, TN 37804
gerald@marlowbx.com
865-412-3396 - O
865-247-5081 - C

```html
<!DOCTYPE html>
<html lang="en">
<head>
<meta charset="utf-8">
<title>Marlow Benefits Consulting — Business Card</title>
<link rel="stylesheet" href="https://fonts.googleapis.com/css2?family=Open+Sans:wght@400;600;700&display=swap">
<style>
  :root {
    --paper: #ebebeb;
    --edge-dark: #505050;
    --band-mid: #6a6a6a;
    --band-dark: #484748;
    --ink: #4a4a4a;
    --accent: #2f8fd0;
    --white: #ffffff;
  }
  html, body {
    margin: 0;
    padding: 0;
    width: 1200px;
    height: 724px;
    overflow: hidden;
    background: var(--paper);
  }
  .card {
    position: relative;
    width: 1200px;
    height: 724px;
    background: var(--paper);
    font-family: "Open Sans", Arial, sans-serif;
    overflow: hidden;
  }
  .edge-top, .edge-bottom {
    position: absolute;
    left: 0;
    width: 100%;
    background: var(--edge-dark);
  }
  .edge-top { top: 0; height: 19px; }
  .edge-bottom { bottom: 0; height: 12px; }
  .contact-band {
    position: absolute;
    left: 0;
    top: 403px;
    width: 100%;
    height: 198px;
    background: var(--band-mid);
  }
  .contact-band__inner {
    position: absolute;
    left: 0;
    top: 20px;
    width: 100%;
    height: 162px;
    background: var(--band-dark);
  }
  .brand {
    position: absolute;
    left: 27px;
    top: 220px;
    display: flex;
    align-items: center;
    gap: 20px;
  }
  .brand__mark {
    width: 136px;
    height: 136px;
    border-radius: 50%;
    background: var(--accent);
  }
  .brand__name {
    color: var(--ink);
    font-weight: 400;
    line-height: 1;
  }
  .brand__primary {
    display: block;
    font-size: 82px;
    letter-spacing: 2px;
  }
  .brand__secondary {
    display: block;
    margin-top: 8px;
    font-size: 20px;
    letter-spacing: 3px;
  }
  .person {
    position: absolute;
    right: 44px;
    top: 252px;
    text-align: right;
  }
  .person__name {
    margin: 0;
    font-size: 60px;
    font-weight: 600;
    letter-spacing: -2px;
    line-height: 1;
    color: var(--ink);
    text-transform: uppercase;
  }
  .person__role {
    margin: 2px 0 0;
    font-size: 24px;
    font-weight: 400;
    line-height: 1;
    color: var(--accent);
  }
  .address {
    position: absolute;
    left: 40px;
    top: 477px;
    margin: 0;
    font-style: normal;
    font-size: 23px;
    font-weight: 600;
    line-height: 33px;
    letter-spacing: -0.5px;
    color: var(--white);
    text-transform: uppercase;
  }
  .reach {
    position: absolute;
    right: 44px;
    top: 475px;
    text-align: right;
    color: var(--white);
  }
  .reach__email {
    display: block;
    font-size: 22px;
    font-weight: 400;
    line-height: 33px;
    letter-spacing: -0.3px;
    text-transform: uppercase;
  }
  .reach__phones {
    display: flex;
    justify-content: flex-end;
    gap: 40px;
    font-size: 20px;
    line-height: 33px;
  }
  .reach__label { margin-right: 10px; }
</style>
</head>
<body>
  <main class="card">
    <div class="edge-top"></div>

    <div class="brand">
      <div class="brand__mark"></div>
      <div class="brand__name">
        <span class="brand__primary">MARLOW</span>
        <span class="brand__secondary">BENEFITS CONSULTING</span>
      </div>
    </div>

    <div class="person">
      <h1 class="person__name">Gerald P Odell</h1>
      <p class="person__role">CEO</p>
    </div>

    <div class="contact-band">
      <div class="contact-band__inner"></div>
    </div>

    <address class="address">
      5172 Brackenfield Road<br>
      Fenwick, TN 37804
    </address>

    <div class="reach">
      <span class="reach__email">gerald@marlowbx.com</span>
      <div class="reach__phones">
        <span><span class="reach__label">(O)</span>(865) 412-3396</span>
        <span><span class="reach__label">(C)</span>(865) 247-5081</span>
      </div>
    </div>

    <div class="edge-bottom"></div>
  </main>
</body>
</html>
```